Clotted cream packaging design (card sleeve over a plain round tub) - family owned UK business.

We require a new design for our clotted cream packaging - (a card sleeve which slips over a plain round tub - photos included to show exactly what the sleeve looks like). This will mainly involve organising the layout with a little bit of scope for some creative work. To tie the design in with our other products we will use the Thornwick Farm logo (This already exists and is attached) - there are no other requirements in regards to tying in with any other of our products. We are looking for something fairly different to our current design (can view it at www.thornwick-example.com).

We are a family owned business producing various dairy products, all of which are handcrafted from start to finish on our organic farm. We are based in North Yorkshire, England.

Our clotted cream is somewhat indulgent/luxurious, the design should subtly reflect this. I’d like it to be fairly clean/minimalistic without forgetting the fact that it is made on a working farm.
Our business is proud of the fact that we’re organic and farm in a sustainable and environmentally friendly way. The word organic needs to be prominent on the side of the sleeve.
The design should use a maximum of 4 colours with the base colour being an off white/cream colour. Our previous design included a purple which I am happy to go with again (although not completely set on it).

Must haves and where it should most likely be placed:

Top (main rounded face):

Logo: Thornwick Farm logo (attatched)
Text: ‘Yorkshire Clotted Cream’ (‘Clotted Cream’ in slightly larger font than ‘Yorkshire’)
Text: ‘113g’ (This is the product weight)

Side/s:

Text: ‘Organic’ ( prominent - both sides)
Text: 'Yorkshire Clotted Cream' (both sides)
Text: ‘Handcrafted on the farm’ (probably just on one side)
Text: ‘Perfect with puds’ (probably just on one side)

Bottom:

Image: Barcode (pdf attached)

Image: Healthmark (oval shape with GB QT842 inside - PDF Attached. Have approx 10mm wide)

Image: BM&K logo (pdf attached - please ensure the height of the BM&K logo is a minimum of 9mm. The colour of this logo can be changed to all black if it works better)

Text: Thornwick Farm, East Calbury, Northallerton, North Yorkshire, ZX9 4QP

Text: ‘All of the milk used to make our clotted cream comes from our own organic cows. Our Indulgent clotted cream is made entirely on farm, from start to finish.’

Text: Ingredients: Fresh organic milk
Allergens: milk

Image: Social media handle & web address (pdf attached)

Text: ‘Keep refrigerated. For best results leave at room temperature for 20 minutes before use.'

Target Market(s)

We predominantly sell in high-end farmshops and deli’s. Targeting people with mid to high disposable income who value the quality and provenance of their food.

Industry/Entity Type

Food

Colors
6B429C
8869AF
B7A5CE
E3DAEB
F3F0F8

Requirements
Must have
• Listed in the project description above. A clean uncluttered design
Nice to have
• Some brands that I quite like: Larkwell Cheddar, Bruna's dairy, The Meadowrun dairy, Cobbles lane cheese.
Should not have
• Not too much going on (not too busy)

```html
<!DOCTYPE html>
<html lang="en">
<head>
<meta charset="utf-8">
<title>Thornwick Farm – Yorkshire Clotted Cream sleeve</title>
<link rel="stylesheet" href="https://fonts.googleapis.com/css2?family=Lexend:wght@100;200;300&display=swap">
<style>
  :root {
    --page-bg: #ffffff;
    --sleeve-cream: #f9f7ef;
    --lavender-soft: #e3daeb;
    --lavender-mid: #b7a5ce;
    --ink: #1b1b1b;
  }
  html, body {
    margin: 0;
    padding: 0;
    width: 1200px;
    height: 900px;
    overflow: hidden;
    background: var(--page-bg);
  }
  .canvas {
    position: relative;
    width: 1200px;
    height: 900px;
    font-family: "Lexend", sans-serif;
    color: var(--ink);
  }
  .sleeve-top {
    position: absolute;
    left: 0;
    top: 0;
    width: 1200px;
    height: 900px;
  }
  .brand-mark {
    position: absolute;
    left: 640px;
    top: 190px;
    transform: rotate(16deg);
    transform-origin: left center;
    font-weight: 300;
    font-size: 34px;
    letter-spacing: 0.14em;
    text-transform: uppercase;
    white-space: nowrap;
  }
  .product-title {
    position: absolute;
    left: 345px;
    top: 215px;
    transform: rotate(27deg);
    transform-origin: left top;
    margin: 0;
    font-weight: 100;
    line-height: 0.95;
    white-space: nowrap;
  }
  .product-title .region {
    display: block;
    font-size: 46px;
    padding-left: 42px;
  }
  .product-title .product {
    display: block;
    font-size: 78px;
    letter-spacing: -0.01em;
  }
  .net-weight {
    position: absolute;
    left: 300px;
    top: 540px;
    transform: rotate(35deg);
    transform-origin: left top;
    font-weight: 200;
    font-size: 28px;
    white-space: nowrap;
  }
</style>
</head>
<body>
<main class="canvas">
  <svg class="sleeve-top" viewBox="0 0 1200 900" xmlns="http://www.w3.org/2000/svg">
    <path class="sleeve-face"
      d="M150 250 Q150 170 230 170 L420 170 Q520 100 620 100 Q720 100 820 170 L970 170 Q1050 170 1050 250 L1050 700 Q1050 780 970 780 L230 780 Q150 780 150 700 Z"
      fill="var(--sleeve-cream)"/>
    <ellipse class="lavender-blob" cx="590" cy="390" rx="330" ry="195"
      transform="rotate(8 590 390)" fill="var(--lavender-soft)"/>
    <circle class="accent-dot" cx="400" cy="230" r="58" fill="var(--lavender-mid)"/>
    <circle class="farm-scene" cx="720" cy="570" r="165" fill="var(--lavender-mid)"
      role="img" aria-label="Line illustration of a farmhouse on rolling fields with cows, trees and a cloud"/>
  </svg>

  <div class="brand-mark">Thornwick Farm</div>

  <h1 class="product-title">
    <span class="region">Yorkshire</span>
    <span class="product">Clotted Cream</span>
  </h1>

  <div class="net-weight">113g/Net</div>
</main>
</body>
</html>
```